Kestrel Photography Business Card

I need a business card designed for a photography business based in Perth, Western Australia called Kestrel Photography.

We specialise in wedding, event photography and portrait photography.

The business card must borrow the style of the attached logo.

The hex codes for the colours in the logo are:
#ED1D85 - Pink
#89C23E - Green
#37282F - Black

The name on the card will be:
Name: Toviran
Phone: 0417395268
Website: www.kestrelphotography.com.au
Facebook: kestrelphotography

I am open and happy to accept creative concepts.

I’d like some space at the back for writing notes and appointment details.

```html
<!DOCTYPE html>
<html lang="en">
<head>
<meta charset="utf-8">
<title>Kestrel Photography Business Card</title>
<link rel="stylesheet" href="https://fonts.googleapis.com/css2?family=Arimo:wght@400&family=Montserrat:wght@700&family=Raleway:wght@400&display=swap">
<style>
  :root {
    --pink: #ED1D85;
    --green: #89C23E;
    --ink: #37282F;
    --paper: #FFFFFF;
    --backdrop: #E4E4E4;
    --muted-text: #4A3A42;
  }
  * { box-sizing: border-box; margin: 0; padding: 0; }
  html, body {
    width: 1200px;
    height: 1000px;
    overflow: hidden;
    background: var(--backdrop);
  }
  .sheet {
    position: relative;
    width: 1200px;
    height: 1000px;
    display: flex;
    flex-direction: column;
    align-items: center;
    justify-content: center;
    gap: 40px;
  }
  .card {
    position: relative;
    width: 770px;
    height: 440px;
    background: var(--paper);
    box-shadow: 0 2px 6px rgba(0,0,0,0.12);
    overflow: hidden;
  }

  /* Front */
  .card-front .brand {
    position: absolute;
    left: 0;
    right: 0;
    top: 196px;
    display: flex;
    align-items: center;
    justify-content: center;
    gap: 22px;
  }
  .brand-dot {
    width: 46px;
    height: 46px;
    border-radius: 50%;
    background: var(--pink);
  }
  .brand-name {
    font-family: "Raleway", sans-serif;
    font-weight: 400;
    font-size: 17px;
    letter-spacing: 0.62em;
    text-transform: uppercase;
    color: var(--ink);
  }

  /* Back */
  .side-band {
    position: absolute;
    left: 0;
    top: 0;
    width: 150px;
    height: 100%;
    background: var(--ink);
  }
  .side-rule {
    position: absolute;
    left: 150px;
    top: 0;
    width: 5px;
    height: 100%;
    background: var(--pink);
  }
  .services {
    position: absolute;
    left: 172px;
    top: 292px;
    list-style: none;
    font-family: "Arimo", sans-serif;
    font-size: 13.5px;
    line-height: 1.35;
    color: var(--muted-text);
  }
  .services li:nth-child(1) { padding-left: 16px; }
  .services li:nth-child(2) { padding-left: 8px; }
  .person-name {
    position: absolute;
    left: 390px;
    top: 168px;
    font-family: "Montserrat", sans-serif;
    font-weight: 700;
    font-size: 21px;
    letter-spacing: 0.12em;
    color: var(--green);
  }
  .contact {
    position: absolute;
    left: 338px;
    top: 282px;
    padding-left: 12px;
    border-left: 2px solid var(--ink);
    list-style: none;
    font-family: "Arimo", sans-serif;
    font-size: 19px;
    color: var(--green);
  }
  .contact li {
    display: flex;
    align-items: center;
    gap: 6px;
    height: 23px;
  }
  .contact-tag {
    display: inline-flex;
    align-items: center;
    justify-content: center;
    width: 18px;
    height: 18px;
    background: var(--pink);
    color: var(--paper);
    font-family: "Arimo", sans-serif;
    font-size: 13px;
    font-weight: 400;
    border-radius: 2px;
  }
</style>
</head>
<body>
<main class="sheet">
  <section class="card card-front" aria-label="Card front">
    <div class="brand">
      <span class="brand-dot" aria-hidden="true"></span>
      <span class="brand-name">Kestrel Photography</span>
    </div>
  </section>

  <section class="card card-back" aria-label="Card back">
    <div class="side-band" aria-hidden="true"></div>
    <div class="side-rule" aria-hidden="true"></div>
    <ul class="services">
      <li>Wedding</li>
      <li>Event Photography</li>
      <li>Portrait Photography</li>
    </ul>
    <p class="person-name">Toviran</p>
    <ul class="contact">
      <li><span class="contact-tag">P</span>0417395268</li>
      <li><span class="contact-tag">W</span>www.kestrelphotography.com.au</li>
      <li><span class="contact-tag" aria-hidden="true"></span>facebook/kestrelphotography</li>
    </ul>
  </section>
</main>
</body>
</html>
```